new hotel menu

help me do do the graphic design for our country pub the coolabah arms in holbrook. the pub has a relaxed australian country feel. here is a copy of our current menu this has our current logo already on it. the numbers after the dishes and discriptions are the prices as i dont often like to use dollar signs. i will also add a couple of quick files that i hit feeding the menu to word mill. i like the feel but not the results. i will also add a file withthe new menu

```html
<!DOCTYPE html>
<html lang="en">
<head>
<meta charset="utf-8">
<title>The Coolabah Arms – Menu</title>
<link rel="stylesheet" href="https://fonts.googleapis.com/css2?family=Josefin+Sans:ital,wght@0,400;0,600;0,700;1,600&display=swap">
<style>
  :root {
    --paper: #ffffff;
    --board: #2b2b2b;
    --rust: #e0603a;
    --cream: #efe2c6;
    --sage: #6f8f5e;
    --bark: #d9c9a3;
    --dash: rgba(224, 96, 58, 0.65);
  }
  * { box-sizing: border-box; margin: 0; padding: 0; }
  html, body {
    width: 1200px; height: 861px; overflow: hidden;
    background: var(--paper);
    font-family: "Josefin Sans", "Century Gothic", sans-serif;
    color: var(--cream);
  }
  .canvas { position: relative; width: 1200px; height: 861px; }

  .board {
    position: absolute; top: 74px; width: 504px; height: 713px;
    background: var(--board);
  }
  .board--left { left: 86px; }
  .board--right { left: 609px; }

  .frame {
    position: absolute; left: 11.5px; right: 11.5px; top: 12.5px; bottom: 13px;
    border: 2px solid var(--rust);
  }
  .divider {
    position: absolute; left: 11.5px; right: 11.5px; height: 2px;
    background: var(--rust);
  }

  /* brand */
  .brand-art {
    position: absolute; left: 200px; top: 29px; width: 100px; height: 43px;
    background: linear-gradient(180deg, #6f8f5e 0%, #d9c9a3 60%, #6f8f5e 100%);
    border-radius: 4px; opacity: 0.85;
  }
  .flourish {
    position: absolute; top: 70px; width: 117px; height: 28px;
    background: var(--sage); opacity: 0.3; border-radius: 14px;
  }
  .flourish--left { left: 43px; }
  .flourish--right { left: 345px; }
  .brand-name {
    position: absolute; left: 0; right: 0; top: 76px;
    text-align: center; font-weight: 600; font-size: 19px; line-height: 22px;
    letter-spacing: 1.5px; color: var(--cream);
  }
  .brand-place {
    position: absolute; left: 0; right: 0; top: 121px;
    text-align: center; font-size: 9px; font-weight: 600; letter-spacing: 1.5px;
    color: var(--cream);
  }

  /* headings */
  .section-title {
    position: absolute; left: 33px; transform: translateY(-50%);
    font-weight: 700; color: var(--rust); line-height: 1;
    font-size: 16px; letter-spacing: 1.6px; white-space: nowrap;
  }
  .section-title::before {
    content: ""; position: absolute; left: -9px; top: 40%;
    width: 3px; height: 3px; border-radius: 50%; background: var(--rust);
  }
  .section-title--large { left: 34px; font-size: 26px; letter-spacing: 1.4px; }
  .section-title--large::before { left: -10px; }
  .sub-title {
    position: absolute; left: 34px; transform: translateY(-50%);
    font-weight: 600; color: var(--cream); font-size: 12.5px; letter-spacing: 1.2px; line-height: 1;
  }
  .sub-title::before {
    content: ""; position: absolute; left: -6px; top: 35%;
    width: 2.5px; height: 2.5px; border-radius: 50%; background: var(--cream);
  }

  .sketch {
    position: absolute; border-radius: 6px;
    background: var(--rust); opacity: 0.3;
  }

  /* item lists */
  .menu-list { position: absolute; left: 34px; width: 436px; list-style: none; --row-h: 12.4px; }
  .item {
    display: grid; grid-template-columns: 20.5px auto 1fr 36px;
    align-items: center; height: var(--row-h);
    border-bottom: 0.7px dashed var(--dash);
  }
  .item--double { height: 23px; }
  .item--tall { height: 24px; }
  .menu-list--roomy { --row-h: 16px; }

  .num, .name, .price, .label {
    font-weight: 600; font-size: 8.6px; letter-spacing: 0.5px; white-space: nowrap;
  }
  .desc {
    font-size: 7.2px; letter-spacing: 0.8px; line-height: 1.1;
    text-align: right; white-space: nowrap; padding-left: 8px;
  }
  .price { display: flex; justify-content: flex-end; font-size: 9px; }
  .item--wide { grid-template-columns: 20.5px auto 1fr 62px; }
  .item--wide .price { margin-right: -4px; }
  .desc--tight { letter-spacing: 0.4px; padding-left: 5px; }

  .split { grid-column: 2 / 4; display: flex; align-items: center; }
  .split--even { justify-content: space-between; }
  .split .desc { padding-left: 0; }
  .push { margin-left: auto; }
  .gap { margin-left: 10px; }

  .footnote {
    position: absolute; left: 34px; top: 676px;
    font-style: italic; font-weight: 600; font-size: 7.6px; letter-spacing: 0.8px;
  }
</style>
</head>
<body>
<main class="canvas">

  <!-- Left board -->
  <section class="board board--left">
    <div class="frame"></div>
    <div class="divider" style="top:305px"></div>
    <div class="divider" style="top:570px"></div>

    <div class="flourish flourish--left" role="img" aria-label="Decorative green swirl flourish"></div>
    <div class="brand-art" role="img" aria-label="Country scene with grazing bull, reeds and river beneath a setting sun"></div>
    <div class="flourish flourish--right" role="img" aria-label="Decorative green swirl flourish"></div>
    <h1 class="brand-name">THE COOLABAH<br>ARMS</h1>
    <p class="brand-place">YARRABEE</p>

    <h2 class="section-title" style="top:157px">STARTERS &amp; SHARES &amp; SIDES</h2>
    <ul class="menu-list" style="top:169px">
      <li class="item"><span class="num">1.</span><span class="name">GARLIC BREAD</span><span class="desc">CLASSIC OR WITH CHEESE &amp; BACON</span><span class="price">9/12</span></li>
      <li class="item"><span class="num">2.</span><span class="name">PUMPKIN + FETA ARANCINI</span><span class="desc">WITH SAGE AND PINE NUT DRESSING</span><span class="price">15</span></li>
      <li class="item"><span class="num">3.</span><span class="name">SALT &amp; PEPPER SQUID</span><span class="desc">WITH AIOLI AND SIDE SALAD</span><span class="price">15</span></li>
      <li class="item"><span class="num">4.</span><span class="name">FRIED PRAWN DUMPLINGS</span><span class="desc">SOY &amp; SESAME DRESSING</span><span class="price">15</span></li>
      <li class="item"><span class="num">5.</span><span class="split split--even"><span class="label">FRIES</span><span class="label">9</span><span class="label">/</span><span class="label">LOADED</span><span class="label">14</span><span class="label">/</span><span class="label">PARMESAN AND ROSEMARY SALT</span></span><span class="price">12</span></li>
      <li class="item"><span class="num">6.</span><span class="name">BRUSCHETTA</span><span class="desc">TOMATO, BASIL, BALSAMIC GLAZE ON TOASTED GARLIC LOAF</span><span class="price">13</span></li>
      <li class="item"><span class="num">7.</span><span class="split"><span class="label">WEDGES</span><span class="desc gap">SOUR CREAM &amp; SWEET CHILLI SAUCE</span><span class="label gap">13</span><span class="desc push">ADD ON FOR BACON AND CHEESE</span></span><span class="price">+3</span></li>
      <li class="item"><span class="num">8.</span><span class="name">MASHED POTATO</span><span class="desc">CREAMY BUTTER MASH</span><span class="price">5</span></li>
      <li class="item"><span class="num">9.</span><span class="name">STEAMED VEGGIES</span><span class="desc">SEASONAL SELECTION</span><span class="price">6</span></li>
      <li class="item"><span class="num">10.</span><span class="name">GARDEN SALAD</span><span class="desc"></span><span class="price">6</span></li>
    </ul>

    <h2 class="section-title" style="top:325px">PUB CLASSICS &amp; MAINS</h2>
    <ul class="menu-list" style="top:338px">
      <li class="item"><span class="num">1.</span><span class="name">BEER-BATTERED FISH &amp; CHIPS</span><span class="desc desc--tight">GUMMY SHARK, HOUSE-MADE BEER BATTER, TARTARE SAUCE</span><span class="price">24</span></li>
      <li class="item item--wide"><span class="num">2.</span><span class="name">LAMB CUTLETS</span><span class="desc">CRUMBED, SERVED WITH MASH AND STEAMED GREENS</span><span class="price">2/28 OR 3/35</span></li>
      <li class="item"><span class="num">3.</span><span class="name">SCOTCH FILLET</span><span class="desc"></span><span class="price">39</span></li>
      <li class="item"><span class="num">4.</span><span class="name">RUMP STEAK</span><span class="desc"><span class="label">400G OR 200G</span></span><span class="price">36/26</span></li>
      <li class="item item--tall"><span class="num">5.</span><span class="name">PHILLY CHEESESTEAK BURGER</span><span class="desc">GRILLED SIRLOIN, CARAMELIZED ONION,<br>SWISS CHEESE, COOLA SPECIAL SAUCE, CHEESE</span><span class="price">26</span></li>
      <li class="item item--tall"><span class="num">6.</span><span class="name">CHICKEN ABC BURGER</span><span class="desc">AVOCADO, BACON, CHEESE, LETTUCE<br>AND SWEET CHILLI MAYO</span><span class="price">25</span></li>
      <li class="item item--tall"><span class="num">7.</span><span class="name">CHICKEN CAESAR SALAD</span><span class="desc">GRILLED OR CRISPY CHICKEN, BACON, PARMESAN,<br>CAESAR DRESSING, COS LETTUCE, CROUTONS, BOILED EGG</span><span class="price">25</span></li>
      <li class="item"><span class="num">8.</span><span class="name">STEAK SANDWICH</span><span class="desc"></span><span class="price">26</span></li>
      <li class="item"><span class="num">9.</span><span class="name">PRAWN AND CHORIZO PASTA</span><span class="desc"></span><span class="price">28</span></li>
      <li class="item"><span class="num">10.</span><span class="split"><span class="label">CARBONARA</span><span class="label push">24</span><span class="desc" style="margin-left:26px">ADD CHICKEN</span></span><span class="price">4</span></li>
      <li class="item"><span class="num">11.</span><span class="name">BEEF AND STOUT PIE</span><span class="desc"></span><span class="price">26</span></li>
      <li class="item"><span class="num">12.</span><span class="name">BANGERS AND MASH</span><span class="desc"></span><span class="price">22</span></li>
      <li class="item"><span class="num">13.</span><span class="name">ROAST OF THE DAY</span><span class="desc"></span><span class="price">22</span></li>
      <li class="item"><span class="num">14.</span><span class="name">GRILLED BARRAMUNDI WITH CARAMELISED LEMON</span><span class="desc"></span><span class="price">30</span></li>
      <li class="item"><span class="num">15.</span><span class="name">CHICKEN SCHNITZEL</span><span class="desc"></span><span class="price">24</span></li>
    </ul>

    <h2 class="section-title" style="top:586px">PARMI MENU</h2>
    <ul class="menu-list" style="top:596px">
      <li class="item"><span class="num">1.</span><span class="name">CLASSIC PARMI</span><span class="desc">NAPOLI SAUCE, HAM, MOZZARELLA</span><span class="price">28</span></li>
      <li class="item"><span class="num">2.</span><span class="name">MEAT LOVERS PARMI</span><span class="desc">BBQ SAUCE, BACON, PEPPERONI, HAM</span><span class="price">29</span></li>
      <li class="item"><span class="num">3.</span><span class="name">ABC PARMI</span><span class="desc">AVOCADO, BACON, CHEESE</span><span class="price">29</span></li>
      <li class="item"><span class="num">4.</span><span class="name">MEXICAN PARMI</span><span class="desc">SALSA, JALAPENOS, SOUR CREAM, CHEESE</span><span class="price">29</span></li>
      <li class="item"><span class="num">5.</span><span class="name">CHOOK ON A HOOK</span><span class="desc">PRAWNS, SQUID IN A CREAMY GARLIC SAUCE</span><span class="price">32</span></li>
      <li class="item"><span class="num">6.</span><span class="name">BUSHMANS</span><span class="desc">MUSHROOM SAUCE, BACON AND CHEESE</span><span class="price">29</span></li>
    </ul>
    <p class="footnote">(ALL SERVED WITH CHIPS &amp; SALAD OR MASH &amp; VEG)</p>
  </section>

  <!-- Right board -->
  <section class="board board--right">
    <div class="frame"></div>
    <div class="divider" style="top:458px"></div>
    <div class="divider" style="top:584px"></div>

    <h2 class="section-title section-title--large" style="top:37px">PIZZA</h2>
    <div class="sketch" style="left:419px;top:24px;width:51px;height:38px" role="img" aria-label="Line sketch of a pizza slice"></div>

    <h3 class="sub-title" style="top:66px">CLASSICS</h3>
    <ul class="menu-list" style="top:74px">
      <li class="item"><span class="num">1.</span><span class="name">MARGHERITA</span><span class="desc">NAPOLI SAUCE, MOZZARELLA, FRESH BASIL</span><span class="price">18</span></li>
      <li class="item"><span class="num">2.</span><span class="name">PEPPERONI</span><span class="desc">NAPOLI SAUCE, DOUBLE PEPPERONI, MOZZARELLA</span><span class="price">22</span></li>
      <li class="item item--double"><span class="num">3.</span><span class="name">BBQ MEAT LOVERS</span><span class="desc">BEEF STRIPS, BACON, PEPPERONI,<br>HAM, BBQ SAUCE AND MOZZARELLA</span><span class="price">26</span></li>
      <li class="item"><span class="num">4.</span><span class="name">HAWAIIAN</span><span class="desc">HAM, PINEAPPLE, MOZZARELLA, NAPOLI SAUCE</span><span class="price">24</span></li>
      <li class="item"><span class="num">5.</span><span class="name">CHEESY GARLIC</span><span class="desc">GARLIC CREAM BASE, MOZZARELLA, OREGANO</span><span class="price">18</span></li>
      <li class="item item--double"><span class="num">6.</span><span class="name">SUPREME</span><span class="desc">HAM, BACON, PEPPERONI, RED ONION, OLIVES, MUSHROOMS,<br>PINEAPPLE AND ROASTED CAPSICUM ON A NAPOLI BASE</span><span class="price">26</span></li>
      <li class="item"><span class="num">7.</span><span class="name">BBQ CHICKEN</span><span class="desc">ROAST CHICKEN, BACON, MUSHROOM AND ONION ON A BBQ BASE</span><span class="price">24</span></li>
    </ul>

    <h3 class="sub-title" style="top:212px">GOURMET SELECTIONS</h3>
    <ul class="menu-list" style="top:217px">
      <li class="item item--double"><span class="num">1.</span><span class="name">GARLIC PRAWN</span><span class="desc">MARINATED PRAWNS, NAPOLI SAUCE,<br>GARLIC CREAM SAUCE, MOZZARELLA</span><span class="price">27</span></li>
      <li class="item item--double"><span class="num">2.</span><span class="name">CHILI CHICKEN</span><span class="desc">MARINATED CHICKEN, JALAPEÑOS, RED ONION,<br>BUFFALO SAUCE AND MOZZARELLA</span><span class="price">23</span></li>
      <li class="item item--double"><span class="num">3.</span><span class="name">VEGGIE SUPREME</span><span class="desc">ROASTED PUMPKIN, FETA, SPINACH,<br>CARAMELIZED ONION, NAPOLI SAUCE</span><span class="price">19</span></li>
      <li class="item item--double"><span class="num">4.</span><span class="name">LOADED CHEESEBURGER</span><span class="desc">SLICED BEEF, PICKLE, ONION, COOLA SPECIAL SAUCE,<br>MOZZARELLA, KETCHUP DRIZZLE</span><span class="price">23</span></li>
    </ul>

    <h3 class="sub-title" style="top:336px">EXTRAS &amp; ADD-ONS</h3>
    <ul class="menu-list menu-list--roomy" style="top:344px">
      <li class="item"><span class="num">1.</span><span class="name">GLUTEN-FREE BASE AVAILABLE</span><span class="desc"></span><span class="price">4</span></li>
      <li class="item"><span class="num">2.</span><span class="name">EXTRA CHEESE 3/ EXTRA MEAT 4/ EXTRA VEGGIES</span><span class="desc"></span><span class="price">3</span></li>
      <li class="item"><span class="num">3.</span><span class="name">SIDE OF HOUSE-MADE CHILLI OIL</span><span class="desc"></span><span class="price"></span></li>
      <li class="item"><span class="num">4.</span><span class="name">PIZZAS AVAILABLE AS HALF &amp; HALF</span><span class="desc"></span><span class="price">2</span></li>
      <li class="item"><span class="num">5.</span><span class="name">ADD SAUCES</span><span class="desc">GRAVY, MUSHROOM, DIANE, PEPPER AND GARLIC SAUCE</span><span class="price">2</span></li>
      <li class="item"><span class="num">6.</span><span class="name">SURF N TURF</span><span class="desc"></span><span class="price">11</span></li>
    </ul>

    <h2 class="section-title section-title--large" style="top:487px">KIDS</h2>
    <div class="sketch" style="left:419px;top:467px;width:51px;height:32px" role="img" aria-label="Line sketch of dumplings"></div>
    <ul class="menu-list" style="top:504px">
      <li class="item"><span class="num">1.</span><span class="name">CHICKEN NUGGETS &amp; CHIPS</span><span class="desc">CRISPY NUGGETS WITH TOMATO SAUCE</span><span class="price">12</span></li>
      <li class="item"><span class="num">2.</span><span class="name">KIDS FISH &amp; CHIPS</span><span class="desc">BATTERED FISH FILLET WITH TARTARE SAUCE</span><span class="price">12</span></li>
      <li class="item"><span class="num">3.</span><span class="name">KIDS SCHNITZEL &amp; CHIPS</span><span class="desc">SMALL CHICKEN SCHNITZEL, GRAVY</span><span class="price">12</span></li>
      <li class="item"><span class="num">4.</span><span class="name">CHEESEY CHEESE PASTA</span><span class="desc">CREAMY CHEESE SAUCE, TOPPED WITH PARMESAN</span><span class="price">12</span></li>
      <li class="item"><span class="num">5.</span><span class="name">KIDS SPAGHETTI BOLOGNESE</span><span class="desc">HOUSE-MADE BEEF BOLOGNESE, PARMESAN</span><span class="price">12</span></li>
    </ul>

    <h2 class="section-title section-title--large" style="top:614px">DESSERTS</h2>
    <div class="sketch" style="left:428px;top:585px;width:40px;height:47px" role="img" aria-label="Line sketch of a dessert cup topped with cream and a cherry"></div>
    <ul class="menu-list" style="top:635px">
      <li class="item"><span class="num">1.</span><span class="name">CHEF'S SPECIAL DESSERT</span><span class="desc">ROTATING SEASONAL SELECTION</span><span class="price">12</span></li>
      <li class="item"><span class="num">2.</span><span class="name">STICKY DATE PUDDING</span><span class="desc">BUTTERSCOTCH SAUCE, WHIPPED CREAM</span><span class="price">12</span></li>
      <li class="item"><span class="num">3.</span><span class="name">NEW YORK CHEESECAKE</span><span class="desc">WITH BERRY COMPOTE</span><span class="price">12</span></li>
      <li class="item"><span class="num">4.</span><span class="name">NANA ROSE'S APPLE PIE</span><span class="desc">WITH ICE CREAM</span><span class="price">12</span></li>
    </ul>
  </section>

</main>
</body>
</html>
```